Restaurant Facility Equipment & Store Maintenance/

I need a flyer showing commercial/industrial kitchen equipment photos we work on Hot Equipment & Cold Equipment and offer many services. see attached highlights

```html
<!DOCTYPE html>
<html lang="en">
<head>
<meta charset="utf-8">
<title>Restaurant Facility Equipment &amp; Store Maintenance</title>
<link href="https://fonts.googleapis.com/css2?family=Poppins:wght@400;500;600;700;800&display=swap" rel="stylesheet">
<style>
:root{
  --navy:#0b2a63;
  --orange:#ff6200;
  --orange-deep:#d94f00;
  --ink:#1e1e1e;
  --page:#b8b8b8;
  --paper:#ffffff;
  --sky:#3d8fd6;
  --rule:#8a8a8a;
}
*{box-sizing:border-box;margin:0;padding:0}
html,body{width:1200px;height:1142px;overflow:hidden;background:var(--page);font-family:'Poppins',sans-serif}
.flyer{position:absolute;left:210px;top:70px;width:780px;height:1008px;background:var(--paper);overflow:hidden;color:var(--ink)}
.abs{position:absolute}
.kitchen-backdrop{left:330px;top:0;width:450px;height:485px;background:linear-gradient(90deg,rgba(255,255,255,1) 0%,#ececec 35%,#d9d9d9 100%)}
.technician{left:425px;top:33px;width:250px;height:452px;border-radius:120px 120px 0 0;background:linear-gradient(180deg,#f2c94c 0%,#9a9a9a 18%,#7d7d7d 60%,#2f3b33 100%)}
.title-lead{left:49px;top:40px;font-size:32px;font-weight:400;letter-spacing:.2px;line-height:1}
.title-main{left:47px;top:82px;font-size:62px;font-weight:800;letter-spacing:-1.5px;line-height:58px;color:var(--navy)}
.title-main .accent{color:var(--orange)}
.title-tail{left:47px;top:200px;font-size:50px;font-weight:400;line-height:1;letter-spacing:-.5px}
.rule{height:1px;background:var(--rule)}
.rule-top{left:49px;top:257px;width:387px}
.rule-mid{left:49px;top:327px;width:400px}
.kitchen-sub{left:49px;top:271px;line-height:1}
.kitchen-sub .small{display:block;font-size:18.5px;font-weight:700;letter-spacing:-.2px}
.kitchen-sub .big{display:block;font-size:24px;font-weight:800;color:var(--navy);margin-top:3px;letter-spacing:-.3px}
.area{left:300px;top:272px;display:flex;gap:6px}
.area p{font-size:12.8px;font-weight:500;line-height:13.6px}
.handle-icon{left:49px;top:344px;width:40px;height:40px;border-radius:8px;background:linear-gradient(135deg,#f5c542,#4a90d9 60%,#e04b3a)}
.handle-head{left:99px;top:342px;font-size:19px;font-weight:700;line-height:23px}
.handle-head span{color:var(--navy)}
.feature{display:flex;gap:6px;font-size:14px;font-weight:500;line-height:16.5px}
.feature svg{flex:none;margin-top:1px}
.band{left:0;top:485px;width:545px;height:170px;background:var(--orange)}
.ring{top:498px;width:142px;height:142px;border-radius:50%;background:var(--orange-deep);box-shadow:0 6px 8px rgba(0,0,0,.18)}
.ring::after{content:"";position:absolute;left:6px;top:6px;width:130px;height:130px;border-radius:50%;border:2px solid #fff}
.photo{position:absolute;left:13px;top:13px;width:116px;height:116px;border-radius:50%}
.photo-fryers{background:linear-gradient(160deg,#cfcfcf,#6e6e6e)}
.photo-tech{background:linear-gradient(160deg,#bfc4cc,#3b4a6b)}
.photo-clean{background:linear-gradient(160deg,#e6e6e6,#4a4a4a)}
.panel{left:545px;top:188px;width:235px;height:467px;background:var(--navy)}
.panel-icon{left:677px;top:237px}
.panel-title{right:61px;top:292px;text-align:right;font-size:19px;font-weight:700;line-height:19.5px;color:#fff}
.panel-title .hot{color:var(--orange)}
.panel-title .cold{color:var(--sky)}
.panel-list{right:62px;top:0;height:100%;list-style:none;text-align:right;color:#fff;font-size:12.3px;font-weight:500;line-height:14px}
.panel-item{position:absolute;right:0;white-space:nowrap}
.panel-item svg{position:absolute;right:-21px;top:2px}
.section-title{font-size:18px;font-weight:800;color:var(--navy);line-height:1;letter-spacing:-.2px}
.section-title span{color:var(--orange)}
.checklist{list-style:none;font-size:12.3px;font-weight:400;line-height:13px}
.checklist li{position:relative;padding-left:17px;margin-bottom:7.4px}
.checklist li svg{position:absolute;left:0;top:1px}
.checklist b{font-weight:700}
.badge-a{left:442px;top:854px;width:103px;height:38px;border-radius:5px;border:3px solid #c8202c;background:#fff}
.badge-b{left:563px;top:858px;width:88px;height:29px;border-radius:15px;background:#2b3b55}
.cta-head{left:49px;top:920px;font-size:17px;font-weight:700;line-height:1;color:var(--ink);letter-spacing:-.1px}
.cta-head span{color:var(--orange)}
.contact{left:49px;top:941px;display:flex;align-items:center;gap:7px;font-size:16.3px;font-weight:400;line-height:22px}
.contact .web{margin-left:10px}
.motto{left:448px;top:923px;width:286px;height:37px;border-radius:8px;background:var(--navy);color:#fff;font-size:11.8px;font-weight:500;display:flex;align-items:center;justify-content:center}
</style>
</head>
<body>
<main class="flyer">
  <div class="abs kitchen-backdrop" role="img" aria-label="Faded commercial kitchen with shelves and range hood"></div>
  <div class="abs technician" role="img" aria-label="Smiling technician in hard hat, gloves and tool belt holding a hammer"></div>

  <h1>
    <span class="abs title-lead">Restaurant Facility</span>
    <span class="abs title-main">EQUIPMENT<br><span class="accent">&amp; STORE</span></span>
    <span class="abs title-tail">MAINTENANCE</span>
  </h1>

  <div class="abs rule rule-top"></div>
  <h2 class="abs kitchen-sub"><span class="small">Commercial &amp; Industrial</span><span class="big">KITCHEN SERVICES</span></h2>
  <div class="abs area">
    <svg width="14" height="18" viewBox="0 0 14 18"><path d="M7 0C3.1 0 0 3 0 6.8 0 11.5 7 18 7 18s7-6.5 7-11.2C14 3 10.9 0 7 0z" fill="var(--orange)"/><circle cx="7" cy="6.8" r="2.8" fill="#fff"/></svg>
    <p>Denver Metro<br>&amp; Surrounding<br>Areas</p>
  </div>
  <div class="abs rule rule-mid"></div>

  <div class="abs handle-icon" role="img" aria-label="Gear, wrench and service van icon"></div>
  <h3 class="abs handle-head">We Handle Everything From<br><span>the Front Door to the Back Door</span></h3>

  <div class="abs feature" style="left:100px;top:397px"><svg width="15" height="15" viewBox="0 0 16 16"><circle cx="8" cy="8" r="6.5" fill="none" stroke="var(--navy)" stroke-width="1.3"/><circle cx="8" cy="8" r="2.5" fill="none" stroke="var(--navy)" stroke-width="1.3"/></svg>Installation</div>
  <div class="abs feature" style="left:236px;top:397px"><svg width="15" height="15" viewBox="0 0 16 16"><circle cx="8" cy="8" r="6.5" fill="none" stroke="var(--navy)" stroke-width="1.3"/><circle cx="8" cy="8" r="3.5" fill="none" stroke="var(--navy)" stroke-width="1.3"/></svg>Rebuilds</div>
  <div class="abs feature" style="left:100px;top:429px"><svg width="15" height="15" viewBox="0 0 16 16"><path d="M3 13l5-5M8 8l4-5 2 2-5 4" fill="none" stroke="var(--navy)" stroke-width="1.4"/><circle cx="4" cy="4" r="2.5" fill="none" stroke="var(--navy)" stroke-width="1.3"/></svg>SafeWork<br>Inspection</div>
  <div class="abs feature" style="left:236px;top:429px"><svg width="15" height="15" viewBox="0 0 16 16"><path d="M8 1l6 2.5v4C14 11 11.5 14 8 15 4.5 14 2 11 2 7.5v-4z" fill="none" stroke="var(--navy)" stroke-width="1.3"/><path d="M8 5l2.5 5h-5z" fill="none" stroke="var(--navy)" stroke-width="1.1"/></svg>Preventive<br>Maintenance Services</div>

  <div class="abs band"></div>
  <div class="abs ring" style="left:66px"><div class="photo photo-fryers" role="img" aria-label="Stainless steel commercial fryers"></div></div>
  <div class="abs ring" style="left:220px"><div class="photo photo-tech" role="img" aria-label="Technician drilling into a kitchen hood"></div></div>
  <div class="abs ring" style="left:374px"><div class="photo photo-clean" role="img" aria-label="Hand wiping an espresso machine"></div></div>

  <aside class="abs panel"></aside>
  <svg class="abs panel-icon" width="43" height="43" viewBox="0 0 43 43">
    <path d="M6 27a14 14 0 0 1 14-14" fill="none" stroke="var(--orange)" stroke-width="4"/>
    <g stroke="var(--orange)" stroke-width="2.6" stroke-linecap="round"><path d="M3 18l4 1.5M10 7l2 4M20 3v4M29 6l-2 4"/></g>
    <g stroke="var(--sky)" stroke-width="2.6" stroke-linecap="round"><path d="M30 18v20M21 28h19M24 22l12 12M36 22l-12 12"/></g>
    <path d="M3 40L40 3" stroke="#fff" stroke-width="2.6" stroke-linecap="round"/>
  </svg>
  <h2 class="abs panel-title"><span class="hot">HOT</span> &amp; <span class="cold">COLD</span><br>EQUIPMENT<br>SERVICES</h2>
  <ul class="abs panel-list">
    <li class="panel-item" style="top:375px">Installation<br>Repair &amp; Rebuilds<svg width="11" height="11" viewBox="0 0 12 12"><circle cx="6" cy="6" r="6" fill="var(--orange)"/><path d="M3.3 6.2l1.9 1.8 3.6-3.7" fill="none" stroke="#fff" stroke-width="1.5"/></svg></li>
    <li class="panel-item" style="top:416px">Preventive<br>Maintenance<br>Programs<svg width="11" height="11" viewBox="0 0 12 12"><circle cx="6" cy="6" r="6" fill="var(--orange)"/><path d="M3.3 6.2l1.9 1.8 3.6-3.7" fill="none" stroke="#fff" stroke-width="1.5"/></svg></li>
    <li class="panel-item" style="top:471px">Equipment Cleaning<br>&amp; Refurbishing<svg width="11" height="11" viewBox="0 0 12 12"><circle cx="6" cy="6" r="6" fill="var(--orange)"/><path d="M3.3 6.2l1.9 1.8 3.6-3.7" fill="none" stroke="#fff" stroke-width="1.5"/></svg></li>
    <li class="panel-item" style="top:512px">OEM Parts with<br>30-Day Warranty<svg width="11" height="11" viewBox="0 0 12 12"><circle cx="6" cy="6" r="6" fill="var(--orange)"/><path d="M3.3 6.2l1.9 1.8 3.6-3.7" fill="none" stroke="#fff" stroke-width="1.5"/></svg></li>
    <li class="panel-item" style="top:554px">Used Equipment<br>Sales &amp; Rentals<svg width="11" height="11" viewBox="0 0 12 12"><circle cx="6" cy="6" r="6" fill="var(--orange)"/><path d="M3.3 6.2l1.9 1.8 3.6-3.7" fill="none" stroke="#fff" stroke-width="1.5"/></svg></li>
    <li class="panel-item" style="top:595px">KSTA-Certified<br>Technicians<svg width="11" height="11" viewBox="0 0 12 12"><circle cx="6" cy="6" r="6" fill="var(--orange)"/><path d="M3.3 6.2l1.9 1.8 3.6-3.7" fill="none" stroke="#fff" stroke-width="1.5"/></svg></li>
  </ul>

  <h2 class="abs section-title" style="left:51px;top:684px">FULL FACILITY <span>SUPPORT</span></h2>
  <ul class="abs checklist" style="left:49px;top:714px">
    <li><svg width="11" height="11" viewBox="0 0 12 12"><circle cx="6" cy="6" r="6" fill="var(--orange)"/><path d="M3.3 6.2l1.9 1.8 3.6-3.7" fill="none" stroke="#fff" stroke-width="1.5"/></svg>Emergency Repairs <b>(24/7 Availability)</b></li>
    <li><svg width="11" height="11" viewBox="0 0 12 12"><circle cx="6" cy="6" r="6" fill="var(--orange)"/><path d="M3.3 6.2l1.9 1.8 3.6-3.7" fill="none" stroke="#fff" stroke-width="1.5"/></svg>SafeWork Inspections</li>
    <li><svg width="11" height="11" viewBox="0 0 12 12"><circle cx="6" cy="6" r="6" fill="var(--orange)"/><path d="M3.3 6.2l1.9 1.8 3.6-3.7" fill="none" stroke="#fff" stroke-width="1.5"/></svg>Handyman Services</li>
    <li><svg width="11" height="11" viewBox="0 0 12 12"><circle cx="6" cy="6" r="6" fill="var(--orange)"/><path d="M3.3 6.2l1.9 1.8 3.6-3.7" fill="none" stroke="#fff" stroke-width="1.5"/></svg>Electrical Upgrades (Licensed Contractor)</li>
    <li><svg width="11" height="11" viewBox="0 0 12 12"><circle cx="6" cy="6" r="6" fill="var(--orange)"/><path d="M3.3 6.2l1.9 1.8 3.6-3.7" fill="none" stroke="#fff" stroke-width="1.5"/></svg>Wall, Floor &amp; Ceiling Repairs</li>
    <li><svg width="11" height="11" viewBox="0 0 12 12"><circle cx="6" cy="6" r="6" fill="var(--orange)"/><path d="M3.3 6.2l1.9 1.8 3.6-3.7" fill="none" stroke="#fff" stroke-width="1.5"/></svg>Painting, Drywall, Door Closers</li>
    <li><svg width="11" height="11" viewBox="0 0 12 12"><circle cx="6" cy="6" r="6" fill="var(--orange)"/><path d="M3.3 6.2l1.9 1.8 3.6-3.7" fill="none" stroke="#fff" stroke-width="1.5"/></svg>Restaurant Furniture Repair/Replacement</li>
    <li><svg width="11" height="11" viewBox="0 0 12 12"><circle cx="6" cy="6" r="6" fill="var(--orange)"/><path d="M3.3 6.2l1.9 1.8 3.6-3.7" fill="none" stroke="#fff" stroke-width="1.5"/></svg>Décor, Signage, Parking Lot &amp; Dumpster Area Repairs</li>
    <li><svg width="11" height="11" viewBox="0 0 12 12"><circle cx="6" cy="6" r="6" fill="var(--orange)"/><path d="M3.3 6.2l1.9 1.8 3.6-3.7" fill="none" stroke="#fff" stroke-width="1.5"/></svg>Food Service Truck Equipment Repairs</li>
  </ul>

  <h2 class="abs section-title" style="left:443px;top:684px">WHY CHOOSE <span>US?</span></h2>
  <ul class="abs checklist" style="left:443px;top:714px">
    <li><svg width="11" height="11" viewBox="0 0 12 12"><circle cx="6" cy="6" r="6" fill="var(--orange)"/><path d="M3.3 6.2l1.9 1.8 3.6-3.7" fill="none" stroke="#fff" stroke-width="1.5"/></svg>KSTA Certified Technicians</li>
    <li><svg width="11" height="11" viewBox="0 0 12 12"><circle cx="6" cy="6" r="6" fill="var(--orange)"/><path d="M3.3 6.2l1.9 1.8 3.6-3.7" fill="none" stroke="#fff" stroke-width="1.5"/></svg>OEM Parts for Maximum Reliability</li>
    <li style="line-height:10.5px"><svg width="11" height="11" viewBox="0 0 12 12"><circle cx="6" cy="6" r="6" fill="var(--orange)"/><path d="M3.3 6.2l1.9 1.8 3.6-3.7" fill="none" stroke="#fff" stroke-width="1.5"/></svg>Preventive Maintenance Subscribers Save<br>on Labor Rates</li>
    <li><svg width="11" height="11" viewBox="0 0 12 12"><circle cx="6" cy="6" r="6" fill="var(--orange)"/><path d="M3.3 6.2l1.9 1.8 3.6-3.7" fill="none" stroke="#fff" stroke-width="1.5"/></svg>Rapid Dispatch of Skilled Technicians</li>
    <li><svg width="11" height="11" viewBox="0 0 12 12"><circle cx="6" cy="6" r="6" fill="var(--orange)"/><path d="M3.3 6.2l1.9 1.8 3.6-3.7" fill="none" stroke="#fff" stroke-width="1.5"/></svg>Local &amp; Trusted in the Denver Metro Area</li>
    <li><svg width="11" height="11" viewBox="0 0 12 12"><circle cx="6" cy="6" r="6" fill="var(--orange)"/><path d="M3.3 6.2l1.9 1.8 3.6-3.7" fill="none" stroke="#fff" stroke-width="1.5"/></svg>Graffiti Removal Services Available</li>
  </ul>
  <div class="abs badge-a" role="img" aria-label="Technician certification badge"></div>
  <div class="abs badge-b" role="img" aria-label="Safety compliance badge"></div>

  <h2 class="abs cta-head"><span>CALL TODAY FOR FAST</span> PROFESSIONAL SERVICE</h2>
  <div class="abs contact">
    <svg width="15" height="15" viewBox="0 0 16 16"><path d="M3.5 1l3 3-1.8 2c1 2 3 4 5 5l2-1.8 3 3-2 2C7 14 2 9 1.5 3z" fill="var(--navy)"/></svg>
    <span>555.014.2290</span>
    <svg class="web" width="16" height="16" viewBox="0 0 16 16" fill="none" stroke="var(--navy)" stroke-width="1.3"><circle cx="8" cy="8" r="7"/><ellipse cx="8" cy="8" rx="3" ry="7"/><path d="M1 8h14M2.5 4.5h11M2.5 11.5h11"/></svg>
    <span>www.hearthlineservice.com</span>
  </div>
  <p class="abs motto">We fix it all — if you have it, we probably fix it.</p>
</main>
</body>
</html>
```